Hollowbrook Yard Services - Needs a business card! Easy JOB!

I need a business card for a new company called Hollowbrook Yard Services. I will be offering the below services.

I am relatively open for ideas, so please be at your creative best.

I think I will list all the services offered on the rear of the card.

- Gardening
- Lawn Care
- Hedge Trimming
- Rubbish Removal
- Weeding/Spraying
- Landscaping
- Gutter Cleaning
- Solar Panel Cleaning
- Irrigation
- Pruning
- On-Site Mulching
- Ask for other services

I am still a little undecided on the colours. I prefer the logos with the Blue text, but I am open for ideas ( the logo/texts colours are not final).

Please use the catch phrase "What can Hollowbrook do for you?"

Here are the required details.

Hollowbrook Yard Services

Miles Fenwarick (owner)
Ph: 1300 555 014
Mob: 0400 555 286

miles@hollowbrookyard.com.au
www.hollowbrookyard.com.au
facebook.com/HollowbrookYard
twitter.com/HollowbrookYard
ABN: 555 019 472 ( this can be in smaller text somewhere, this is the least important )

Thankyou in advance! And good luck.

regards,
Miles
Updates

Hi everyone, please make sure you include the phrase "What can Hollowbrook do for you?" on the designs.

thanks,
Miles

Definitely liking the focus on a majority of the design on the blue colour from the logo. Also a splash of green in the plant.

Please make sure you list the services provided on the rear of the card. thanks.

With the service listing, please make "ask for other services" stand out, either a different colour or position or size... as long as it is more noticeable than the other services listed. Thanks.

Industry/Entity Type

Business

Requirements
Must have
• - use the font supplied (Brandon Family Font)
- use of the catch phrase "What can Hollowbrook do for you?"
- Double sided design
- Chatterly and Quipster logos/links
- Please use symbol/picture for "phone" "mobile" "email" instead of using the words.
- List the services provided on the rear of the card

```html
<!DOCTYPE html>
<html lang="en">
<head>
<meta charset="utf-8">
<title>Hollowbrook Yard Services – Business Card</title>
<link rel="stylesheet" href="https://fonts.googleapis.com/css2?family=Josefin+Sans:wght@300;400;600;700&display=swap">
<style>
  :root {
    --page-bg: #e9eaec;
    --card-white: #ffffff;
    --navy: #173a78;
    --brand-blue: #1f5fae;
    --sky: #5ea8de;
    --sky-soft: #8cc3ea;
    --grey-text: #a3a5a8;
    --ink: #3c3d40;
  }
  * { box-sizing: border-box; margin: 0; padding: 0; }
  html, body {
    width: 1141px;
    height: 1200px;
    overflow: hidden;
    background: var(--page-bg);
    font-family: "Josefin Sans", sans-serif;
  }
  .sheet {
    position: relative;
    width: 1141px;
    height: 1200px;
  }
  .card {
    position: absolute;
    left: 120px;
    width: 900px;
    height: 550px;
    box-shadow: 0 10px 28px rgba(0,0,0,0.18);
  }

  /* ---------- Front ---------- */
  .card-front {
    top: 40px;
    background: var(--card-white);
  }
  .tagline {
    position: absolute;
    left: 80px;
    top: 80px;
    font-size: 46px;
    line-height: 1.12;
    font-weight: 300;
    letter-spacing: 2px;
    text-transform: uppercase;
    color: var(--grey-text);
  }
  .tagline strong { font-weight: 700; }
  .brand-mark {
    position: absolute;
    left: 540px;
    top: 190px;
    display: flex;
    align-items: center;
    gap: 16px;
  }
  .brand-mark .dot {
    width: 40px;
    height: 40px;
    border-radius: 50%;
    background: var(--sky);
    flex: none;
  }
  .brand-mark .name {
    font-size: 34px;
    line-height: 1.05;
    font-weight: 700;
    text-transform: uppercase;
    color: var(--brand-blue);
    width: 280px;
  }
  .owner {
    position: absolute;
    right: 60px;
    top: 380px;
    text-align: right;
    font-size: 24px;
    color: var(--brand-blue);
  }
  .owner .person { font-weight: 700; }
  .owner .role { color: var(--ink); font-weight: 400; }
  .phones {
    position: absolute;
    right: 60px;
    top: 420px;
    font-size: 22px;
    color: var(--ink);
  }
  .phones .label { color: var(--brand-blue); }
  .web-line {
    position: absolute;
    left: 80px;
    bottom: 44px;
    font-size: 19px;
    color: var(--ink);
  }
  .web-line .sep { color: var(--grey-text); padding: 0 6px; }

  /* ---------- Back ---------- */
  .card-back {
    top: 610px;
    background: var(--navy);
  }
  .brand-emblem {
    position: absolute;
    left: 70px;
    top: 50px;
    display: flex;
    align-items: center;
    gap: 20px;
  }
  .brand-emblem .dot {
    width: 150px;
    height: 150px;
    border-radius: 50%;
    background: var(--sky);
  }
  .brand-emblem .name {
    font-size: 34px;
    font-weight: 700;
    line-height: 1.05;
    text-transform: uppercase;
    color: var(--sky);
    width: 260px;
  }
  .social {
    position: absolute;
    left: 440px;
    top: 248px;
    display: flex;
    align-items: center;
    gap: 14px;
    font-size: 22px;
    color: var(--sky);
  }
  .social .network {
    display: flex;
    align-items: center;
    gap: 8px;
  }
  .social .square {
    width: 22px;
    height: 22px;
    background: var(--sky);
    border-radius: 3px;
  }
  .services {
    position: absolute;
    left: 0;
    right: 0;
    top: 318px;
    text-align: center;
    list-style: none;
    font-size: 26px;
    line-height: 1.4;
    color: #ffffff;
  }
  .services .bullet {
    display: inline-block;
    width: 9px;
    height: 9px;
    border-radius: 50%;
    background: var(--sky);
    margin: 0 12px;
    vertical-align: middle;
    position: relative;
    top: -3px;
  }
  .services .more {
    color: var(--sky);
    font-size: 27px;
    font-weight: 600;
  }
</style>
</head>
<body>
<main class="sheet">

  <section class="card card-front" aria-label="Business card front">
    <h1 class="tagline">What can<br><strong>Hollowbrook</strong><br>do for you?</h1>

    <div class="brand-mark">
      <span class="dot"></span>
      <span class="name">Hollowbrook Yard Services</span>
    </div>

    <p class="owner"><span class="person">Miles Fenwarick</span> <span class="role">Owner</span></p>
    <p class="phones"><span class="label">Ph</span> 1300 555 014 &nbsp;<span class="label">Mob</span> 0400 555 286</p>
    <p class="web-line">miles@hollowbrookyard.com.au<span class="sep">||</span>www.hollowbrookyard.com.au</p>
  </section>

  <section class="card card-back" aria-label="Business card back">
    <div class="brand-emblem">
      <span class="dot"></span>
      <span class="name">Hollowbrook Yard Services</span>
    </div>

    <div class="social">
      <span class="network"><span class="square"></span>Chatterly</span>
      <span class="network"><span class="square"></span>Quipster</span>
      <span>/HollowbrookYard</span>
    </div>

    <ul class="services">
      <li>Gardening<span class="bullet"></span>Lawn Care<span class="bullet"></span>Hedge Trimming<span class="bullet"></span>Rubbish Removal</li>
      <li>Weeding/Spraying<span class="bullet"></span>Landscaping<span class="bullet"></span>Gutter Cleaning</li>
      <li>Solar Panel Cleaning<span class="bullet"></span>Irrigation<span class="bullet"></span>Pruning<span class="bullet"></span>On-Site Mulching</li>
      <li class="more">Ask for other services</li>
    </ul>
  </section>

</main>
</body>
</html>
```